A Flyer for a clinic/hospital waiting room to warn about patients that they must not abuse our staff

we need a flyer (text attached) with a background of a female nurse or medical doctor photo. I like the example photo where there are four headless satff lined up - something like this, indicating that we are a team and will not tolerate abuse
A4
the text will be over the photo.

Target Market(s)

patients who come to our clinic

Industry/Entity Type

medicine - urology

Colors
0054AA
0677BA
7BADD7
CADEEF
E8F1F8
0094D4
00A9DD
6FCCEA
C7EBF8
E9F6FB

Requirements
Must have
• a photo taking up the whole A4, and text over this. The photos I haev sent are just examples - I will need yo to source a photo
Nice to have
• Horizontal A4 and vertical A4 options. Please add our logo in small , in the bottom right corner

```html
<!DOCTYPE html>
<html lang="en">
<head>
<meta charset="utf-8">
<title>Zero Tolerance Flyer</title>
<link rel="stylesheet" href="https://fonts.googleapis.com/css2?family=Montserrat:wght@300;400;500;600;700;800;900&display=swap">
<style>
  :root {
    --backdrop: #143a63;
    --page: #eef2f8;
    --navy: #0054AA;
    --sky: #5aa2dc;
    --sky-deep: #2f78bf;
    --ink: #111418;
    --body: #1e2530;
    --logo: #55606c;
    --bullet: #0054AA;
  }
  * { margin: 0; padding: 0; box-sizing: border-box; }
  html, body { width: 1200px; height: 1200px; overflow: hidden; }
  body {
    background: var(--backdrop);
    font-family: "Montserrat", sans-serif;
    position: relative;
  }
  .flyer {
    position: absolute;
    left: 206px; top: 47px;
    width: 788px; height: 1105px;
    background: var(--page);
    overflow: hidden;
  }
  .flyer-photo {
    position: absolute; inset: 0;
    background:
      linear-gradient(100deg, rgba(160,190,225,0.75) 0%, rgba(190,210,235,0.55) 30%, rgba(230,236,246,0.35) 55%, rgba(240,243,249,0.2) 100%),
      radial-gradient(ellipse at 85% 25%, #f4f6fa 0%, #e6ebf3 50%, #dfe6f0 100%);
  }
  .flyer-veil {
    position: absolute; inset: 0;
    background: linear-gradient(180deg, rgba(240,244,250,0.25) 0%, rgba(240,244,250,0.45) 60%, rgba(240,244,250,0.6) 100%);
  }
  .intro {
    position: absolute; top: 66px; left: 0; width: 100%;
    text-align: center;
    font-size: 31px; font-weight: 400; color: var(--ink);
    letter-spacing: 0.3px;
  }
  .intro strong { font-weight: 800; }
  .headline {
    position: absolute; top: 112px; left: 0; width: 100%;
    text-align: center;
    font-size: 63px; font-weight: 900; color: var(--sky);
    letter-spacing: -0.5px;
    text-shadow: 1px 2px 0 var(--sky-deep);
  }
  .tagline {
    position: absolute; top: 196px; left: 70px;
    width: 648px; height: 29px;
    background: var(--navy);
    border-radius: 8px;
    color: #fff;
    font-size: 17px; font-weight: 700;
    text-align: center; line-height: 29px;
  }
  .definition {
    position: absolute; top: 301px; left: 73px;
    width: 640px; height: 324px;
    border: 2px solid #fff;
    border-radius: 10px;
  }
  .definition-title {
    position: absolute; top: -14px; left: 28px;
    padding: 0 8px;
    font-size: 20px; font-weight: 300; color: var(--ink);
    background: transparent;
    text-shadow: 0 0 6px rgba(235,240,248,0.9);
  }
  .definition ul {
    list-style: none;
    position: absolute; top: 46px; left: 26px;
  }
  .definition li {
    font-size: 21px; font-weight: 600; color: var(--ink);
    height: 39px; line-height: 28px;
    position: relative; padding-left: 17px;
  }
  .definition li::before {
    content: ""; position: absolute; left: 0; top: 13px;
    width: 7px; height: 7px; border-radius: 50%;
    background: var(--bullet);
  }
  .policy {
    position: absolute; left: 50px; width: 688px;
    font-size: 18px; font-weight: 400; color: var(--body);
    line-height: 29.5px; text-align: center;
  }
  .policy.consequences { top: 660px; }
  .policy.support { top: 773px; }
  .policy.reason { top: 854px; text-align: justify; text-align-last: center; }
  .brand {
    position: absolute; right: 26px; top: 1010px;
    display: flex; align-items: center; gap: 8px;
    font-size: 22px; font-weight: 500; color: var(--logo);
  }
  .brand-dot {
    width: 14px; height: 14px; border-radius: 50%;
    background: var(--sky);
  }
</style>
</head>
<body>
  <main class="flyer">
    <div class="flyer-photo" role="img" aria-label="Background photo of a medical team in light blue scrubs standing with arms crossed, one wearing a stethoscope"></div>
    <div class="flyer-veil"></div>

    <p class="intro">We have <strong>zero-tolerance</strong> for any form of</p>
    <h1 class="headline">Aggressive Behaviour</h1>
    <p class="tagline">Our staff treat you with respect and we expect the same in return.</p>

    <section class="definition">
      <h2 class="definition-title">Aggressive behaviour (in-person or on the telephone) is:</h2>
      <ul>
        <li>Verbal harassment</li>
        <li>Any verbal or physical confrontation</li>
        <li>Raising your voice or making unreasonable demands</li>
        <li>Abusive or intimidating behaviour</li>
        <li>Sexual or suggestive language or behaviour</li>
        <li>Making threats to our staff</li>
        <li>Swearing</li>
      </ul>
    </section>

    <p class="policy consequences">If any of our staff feel intimidated in any way, we will always support them. Incidents will result in your immediate removal from the facility, termination of your relationship with the practice, and may result in prosecution.</p>
    <p class="policy support">In all circumstances we will support any staff member who wishes to press charges against a perpetrator of aggressive behaviour.</p>
    <p class="policy reason">We take this stance because our staff work extremely hard in busy circumstances to help you and we will no longer tolerate any form of aggression or abuse.</p>

    <div class="brand"><span class="brand-dot"></span>Riverbend Urology</div>
  </main>
</body>
</html>
```